Media and Film Company Needs a New Website

We produce highly stylized commercials and film pieces for our clients. We also produce live events, both corporate and theatrical. Looking for a site that can show off our client videos - have a polished way to show off our team, and be able to create pages to highlight our clients and give a full overview of our project/process with them. We design simple website for some of our clients - so we are very wordpress familiar, and would like something that doesn't feel like a template.

Target Market(s)

content creators, creative directors, production teams, marketing agencies

Industry/Entity Type

Film Production

Number of Pages Required

4 page

Font styles to use
Sans Serif

Requirements
Must have
• slick looking video embed (from YT or Vimeo)
• project pages - client snapshot (what we did for them, how we did it)
• nice landing page, have our company video reel on the page
• testimonials
• contact page
• ability to have photos as a background if we want
Nice to have
• polished clean look - look to our logo colors and linear elements
• we produce very stylized videos for our clients and our website should reflect that
Should not have
• template look or feel to it- please bring your flare to the project!
• take a look at our current site - zantorvo.com we need a better way to highlight our work and our clients

```html
<!DOCTYPE html>
<html lang="en">
<head>
<meta charset="utf-8">
<title>Zantorvo Media &amp; Entertainment</title>
<link href="https://fonts.googleapis.com/css2?family=Raleway:wght@500;600;700;800&family=Open+Sans:wght@400;600&family=Roboto+Condensed:wght@400;700&display=swap" rel="stylesheet">
<style>
:root{
  --gold:#d9a81c;
  --pink:#d6287f;
  --ink:#1b1b1b;
  --text:#6f6f6f;
  --line:#dcdcdc;
  --footer:#1a1616;
  --white:#ffffff;
}
*{box-sizing:border-box;margin:0;padding:0}
html,body{width:1200px;height:2671px;overflow:hidden;background:var(--white)}
body{position:relative;font-family:"Open Sans",sans-serif;color:var(--ink)}
.abs{position:absolute}
/* header */
.site-header{top:0;left:0;width:1200px;height:92px;background:var(--white)}
.brand{left:98px;top:30px;display:flex;align-items:center;gap:10px}
.brand-dot{width:14px;height:14px;background:var(--pink)}
.brand-name{font-family:"Raleway",sans-serif;font-weight:800;font-size:26px;letter-spacing:1px;color:var(--ink);line-height:1}
.brand-sub{font-family:"Raleway",sans-serif;font-size:11px;font-weight:600;color:var(--ink);margin-top:3px}
.main-nav{right:98px;top:42px;display:flex;gap:38px;font-size:13px;color:#333;text-transform:uppercase}
.main-nav .active{color:var(--pink)}
/* hero */
.hero{top:92px;left:0;width:1200px;height:468px;background:linear-gradient(180deg,#4b3a8c 0%,#7b4aa0 25%,#a0786a 55%,#4f5f86 80%,#1d2a4a 100%)}
.hero-title{top:218px;left:0;width:1200px;text-align:center;font-family:"Raleway",sans-serif;font-weight:700;font-size:44px;line-height:62px;color:var(--white);letter-spacing:1px}
.hero-btn{top:374px;left:538px;width:124px;height:44px;background:var(--gold);color:var(--white);font-size:13px;text-align:center;line-height:44px;font-weight:600}
.hero-arrow{width:34px;height:34px;background:rgba(255,255,255,.25);display:flex;align-items:center;justify-content:center}
/* about */
.about-title{top:620px;left:98px;font-family:"Raleway",sans-serif;font-weight:600;font-size:22px;letter-spacing:.5px}
.about-text{top:662px;left:98px;width:535px;font-size:12.5px;line-height:24px;color:var(--text)}
.btn{height:42px;line-height:40px;font-size:13px;font-weight:600;text-align:center;text-transform:uppercase}
.btn-solid{background:var(--gold);color:var(--white);border:1px solid var(--gold)}
.btn-outline{border:1px solid var(--gold);color:var(--gold)}
.about-photo{top:628px;left:670px;width:428px;height:222px;background:linear-gradient(135deg,#2a1a14,#8a4a1c 45%,#d8803a 60%,#201010);box-shadow:0 2px 8px rgba(0,0,0,.2);border:4px solid #fff}
.gold-rule{top:912px;left:0;width:1200px;height:2px;background:var(--gold)}
/* videos */
.section-title{left:0;width:1200px;text-align:center;font-family:"Raleway",sans-serif;font-weight:600;font-size:26px;letter-spacing:.5px}
.video-card{top:1043px;width:314px}
.video-thumb{height:255px;position:relative}
.video-bar{position:absolute;left:0;bottom:0;width:100%;height:12px;background:rgba(0,0,0,.55)}
.video-play{position:absolute;left:8px;bottom:3px;width:0;height:0;border-left:7px solid #fff;border-top:4px solid transparent;border-bottom:4px solid transparent}
.video-title{margin-top:20px;font-family:"Raleway",sans-serif;font-weight:600;font-size:15px;color:var(--ink)}
.video-meta{margin-top:14px;display:flex;justify-content:space-between;align-items:center;font-size:12px;color:var(--gold)}
.client-name{font-family:"Open Sans",sans-serif;font-weight:600;font-size:13px;color:#2c3e6b}
.slider-arrow{top:1200px;font-size:22px;color:#222}
/* services */
.services{top:1426px;left:0;width:1200px;height:452px;background:linear-gradient(90deg,#5a1c3a 0%,#7a4a2e 35%,#9a7a18 55%,#24405a 85%,#16304a 100%)}
.services-title{top:1493px;left:0;width:1200px;text-align:center;font-family:"Raleway",sans-serif;font-weight:500;font-size:26px;color:var(--white)}
.services-rule{top:1538px;left:578px;width:44px;height:2px;background:var(--white)}
.service{top:1601px;width:200px;text-align:center;color:var(--white)}
.service-label{margin-top:8px;font-size:14px;font-weight:600;line-height:21px;text-transform:uppercase}
/* testimonials */
.testi-nav{top:1968px;display:flex;gap:10px}
.testi-nav span{width:26px;height:26px;border:1px solid #ccc;display:flex;align-items:center;justify-content:center;font-size:14px}
.testi-card{top:2020px;width:484px;height:198px;border:1px solid var(--line);padding:26px 30px 0 58px}
.quote-mark{position:absolute;left:20px;top:18px;font-family:Georgia,serif;font-size:30px;font-weight:700;color:#333;line-height:1}
.testi-name{font-size:14px;font-weight:600;text-transform:uppercase}
.testi-name em{font-size:11px;text-transform:none;font-weight:400}
.testi-date{margin-top:4px;font-size:11px;color:var(--gold)}
.testi-text{margin-top:10px;font-size:12px;line-height:22px;color:var(--text)}
.avatar{position:absolute;right:20px;bottom:-40px;width:82px;height:82px;border-radius:50%;border:3px solid #fff;background:linear-gradient(160deg,#3c6aa8,#c79a7a)}
/* footer */
.site-footer{top:2313px;left:0;width:1200px;height:358px;background:var(--footer);color:var(--white)}
.foot-head{top:2368px;font-family:"Roboto Condensed",sans-serif;font-size:18px}
.foot-list{top:2412px;font-size:12.5px;line-height:37px}
.foot-list li{list-style:none;padding-left:20px;position:relative}
.foot-list li::before{content:"»";position:absolute;left:0}
.contact-row{display:flex;gap:16px;font-size:12.5px;line-height:20px}
.news-text{top:2412px;left:831px;font-size:11.5px}
.news-input{top:2442px;left:831px;width:270px;height:40px;background:#fff;color:#444;font-size:11px;padding:12px 14px}
.news-btn{top:2492px;left:831px;width:100px;height:42px;background:var(--gold);font-size:12px;font-weight:600;text-align:center;line-height:42px}
.foot-rule{top:2598px;left:0;width:1200px;height:1px;background:#333}
.copyright{top:2622px;left:98px;font-size:11.5px}
.socials{top:2619px;left:972px;display:flex;gap:10px}
.socials span{width:23px;height:23px;border-radius:50%;background:#fff}
</style>
</head>
<body>

<header class="site-header abs">
  <div class="brand abs">
    <span class="brand-dot"></span>
    <div>
      <div class="brand-name">ZANTORVO</div>
      <div class="brand-sub">Media &amp; Entertainment</div>
    </div>
  </div>
  <nav class="main-nav abs">
    <span class="active">Home</span><span>Portfolio</span><span>About Zantorvo</span><span>Testimonials</span><span>Press</span><span>Contact Us</span>
  </nav>
</header>

<section class="hero abs" role="img" aria-label="Concert crowd with raised hands under purple stage lights"></section>
<h1 class="hero-title abs">WELCOME TO ZANTORVO MEDIA &amp;<br>ENTERTAINMENT</h1>
<div class="hero-btn abs">GET STARTED</div>
<div class="hero-arrow abs" style="left:52px;top:309px"><svg width="10" height="12"><path d="M8 1 2 6 8 11" stroke="#222" stroke-width="2" fill="none"/></svg></div>
<div class="hero-arrow abs" style="left:1110px;top:309px"><svg width="10" height="12"><path d="M2 1 8 6 2 11" stroke="#222" stroke-width="2" fill="none"/></svg></div>

<h2 class="about-title abs">ABOUT ZANTORVO MEDIA &amp; ENTERTAINMENT</h2>
<p class="about-text abs">Zantorvo Media &amp; Entertainment provides full-service campaigns in film and media production, live entertainment &amp; theatrical production, marketing &amp; advertising, and event management in the DC metro area. Founded in 2009, Zantorvo Media &amp; Entertainment has built a reputation working for clients including the Harborline Film Institute, SLN, Calder Music, Rivermouth Community Resources, and Brightwell Events.</p>
<div class="btn btn-solid abs" style="top:808px;left:98px;width:105px">Read More</div>
<div class="btn btn-outline abs" style="top:808px;left:211px;width:113px">Contact Us</div>
<div class="about-photo abs" role="img" aria-label="Performers on a bar stage under warm orange lighting"></div>
<div class="gold-rule abs"></div>

<h2 class="section-title abs" style="top:968px">OUR CLIENT VIDEOS</h2>
<div class="slider-arrow abs" style="left:52px"><svg width="10" height="14"><path d="M8 1 2 7 8 13" stroke="#222" stroke-width="2" fill="none"/></svg></div>
<div class="slider-arrow abs" style="left:1124px"><svg width="10" height="14"><path d="M2 1 8 7 2 13" stroke="#222" stroke-width="2" fill="none"/></svg></div>

<article class="video-card abs" style="left:98px">
  <div class="video-thumb" role="img" aria-label="Conference stage with large lettering in dark blue light" style="background:linear-gradient(135deg,#0e1620,#3a4656 55%,#1a222c)"><span class="video-bar"></span><span class="video-play"></span></div>
  <div class="video-title">2017 SLN SUMMIT Concludes In Lakeport</div>
  <div class="video-meta"><span>By Dana Whitcombe</span><span class="client-name">SLN</span></div>
</article>
<article class="video-card abs" style="left:443px">
  <div class="video-thumb" role="img" aria-label="Two chefs teaching a cooking class" style="background:linear-gradient(135deg,#3a2a22,#b8a490 50%,#5a3a2a)"><span class="video-bar"></span><span class="video-play"></span></div>
  <div class="video-title">Class at Saporia Cooking School!</div>
  <div class="video-meta"><span>By Saporia</span><span class="client-name" style="color:#6a3a8a">Saporia</span></div>
</article>
<article class="video-card abs" style="left:786px">
  <div class="video-thumb" role="img" aria-label="Musicians playing at a jazz jam session" style="background:linear-gradient(135deg,#4a4030,#8a8070 50%,#2a2a24)"><span class="video-bar"></span><span class="video-play"></span></div>
  <div class="video-title">The Calder jazz jam for musicians</div>
  <div class="video-meta"><span>By Calder Jazz Jam</span><span class="client-name" style="color:#b2262a">Calder</span></div>
</article>

<section class="services abs" role="img" aria-label="Speaker at a podium in front of flags, tinted magenta to blue"></section>
<h2 class="services-title abs">WHAT WE DO</h2>
<div class="services-rule abs"></div>

<div class="service abs" style="left:125px">
  <svg width="200" height="150" viewBox="0 0 200 150"><rect x="48" y="22" width="104" height="104" transform="rotate(45 100 74)" fill="none" stroke="#fff" stroke-width="1.5"/><rect x="82" y="66" width="28" height="20" fill="#fff"/><path d="M110 72 122 65 V88 L110 81Z" fill="#fff"/><circle cx="88" cy="60" r="5" fill="#fff"/><circle cx="102" cy="60" r="5" fill="#fff"/></svg>
  <div class="service-label">Film &amp; Media<br>Production</div>
</div>
<div class="service abs" style="left:375px">
  <svg width="200" height="150" viewBox="0 0 200 150"><rect x="48" y="22" width="104" height="104" transform="rotate(45 100 74)" fill="none" stroke="#fff" stroke-width="1.5"/><path d="M84 70H116L112 90H88Z" fill="#fff"/><circle cx="100" cy="76" r="5" fill="none" stroke="#5a3a2a" stroke-width="1.5"/><path d="M100 70V56" stroke="#fff" stroke-width="2"/><circle cx="100" cy="55" r="3" fill="#fff"/></svg>
  <div class="service-label">Live<br>Production</div>
</div>
<div class="service abs" style="left:625px">
  <svg width="200" height="150" viewBox="0 0 200 150"><rect x="48" y="22" width="104" height="104" transform="rotate(45 100 74)" fill="none" stroke="#fff" stroke-width="1.5"/><circle cx="100" cy="76" r="15" fill="none" stroke="#fff" stroke-width="2"/><ellipse cx="100" cy="76" rx="6" ry="15" fill="none" stroke="#fff" stroke-width="2"/><path d="M85 76H115" stroke="#fff" stroke-width="2"/><circle cx="115" cy="61" r="4" fill="#fff"/></svg>
  <div class="service-label">PR, Marketing &amp;<br>Advertising</div>
</div>
<div class="service abs" style="left:875px">
  <svg width="200" height="150" viewBox="0 0 200 150"><rect x="48" y="22" width="104" height="104" transform="rotate(45 100 74)" fill="none" stroke="#fff" stroke-width="1.5"/><rect x="85" y="62" width="30" height="28" fill="none" stroke="#fff" stroke-width="2"/><path d="M85 69H115M92 58V66M108 58V66" stroke="#fff" stroke-width="2"/><circle cx="114" cy="88" r="6" fill="#fff"/></svg>
  <div class="service-label">Events</div>
</div>

<h2 class="section-title abs" style="top:1928px">TESTIMONIALS</h2>
<div class="testi-nav abs" style="left:1030px"><span>‹</span><span>›</span></div>

<article class="testi-card abs" style="left:98px">
  <span class="quote-mark">“</span>
  <div class="testi-name">Marcus Penfield, <em>Executive Director</em></div>
  <div class="testi-date">MAR 12 , 2017</div>
  <p class="testi-text">Thank you very much for all the hard work and creativity that you devoted to the RCR video, which was moving Hollis......</p>
  <div class="avatar" role="img" aria-label="Portrait of the client"></div>
</article>
<article class="testi-card abs" style="left:615px">
  <span class="quote-mark">“</span>
  <div class="testi-name">Alan Mercer , <em>Executive Director</em></div>
  <div class="testi-date">MAR 12 , 2017</div>
  <p class="testi-text">Te vix tation mucius, nec suas latine commodo in. Omnium indoctum ei nam. Vel ne quidam volutpat euripidis Ei est quis.....</p>
  <div class="avatar" role="img" aria-label="Portrait of the client" style="background:linear-gradient(160deg,#3c6aa8,#d0a080)"></div>
</article>

<footer class="site-footer abs"></footer>
<div class="foot-head abs" style="left:98px;color:#fff">CONTACT US</div>
<div class="foot-head abs" style="left:385px;color:#fff">QUICK LINKS</div>
<div class="foot-head abs" style="left:636px;color:#fff">OTHER LINKS</div>
<div class="foot-head abs" style="left:831px;color:#fff">SIGN UP TO NEWSLETTER</div>

<div class="abs" style="top:2415px;left:98px;color:#fff">
  <div class="contact-row"><svg width="18" height="22" viewBox="0 0 18 22"><path d="M9 21C9 21 2 13 2 8a7 7 0 0 1 14 0c0 5-7 13-7 13Z" fill="none" stroke="#fff" stroke-width="1.5"/><circle cx="9" cy="8" r="2.5" fill="none" stroke="#fff" stroke-width="1.5"/></svg><span>Zantorvo Media &amp; Entertainment<br>4410 Lantern Road #210<br>Fairhaven, MD 20901</span></div>
  <div class="contact-row" style="margin-top:18px"><svg width="18" height="18" viewBox="0 0 18 18"><path d="M4 2 7 6 5 8c1 2 3 4 5 5l2-2 4 3-2 3C8 17 1 10 1 4Z" fill="none" stroke="#fff" stroke-width="1.5"/></svg><span>Phone : +1 555 014 2287</span></div>
  <div class="contact-row" style="margin-top:16px"><svg width="18" height="14" viewBox="0 0 18 14"><rect x="1" y="1" width="16" height="12" fill="none" stroke="#fff" stroke-width="1.5"/><path d="M1 1 9 8 17 1" fill="none" stroke="#fff" stroke-width="1.5"/></svg><span>Email : info@zantorvo.com</span></div>
</div>
<ul class="foot-list abs" style="left:385px;color:#fff"><li>Home</li><li>Portfolio</li><li>About Zantorvo</li><li>Testimonials</li></ul>
<ul class="foot-list abs" style="left:636px;color:#fff"><li>Press</li><li>Contact Us</li><li>Privacy Policy</li><li>Terms and Conditions</li></ul>
<div class="news-text abs" style="color:#fff">Excepteur sint occaecat cupidatat non proident.</div>
<div class="news-input abs">Enter Name</div>
<div class="news-btn abs" style="color:#fff">SUBSCRIBE</div>
<div class="foot-rule abs"></div>
<div class="copyright abs" style="color:#fff">@copyright 2017 Zantorvo Media &amp; Entertainment.All Rights Reserved</div>
<div class="socials abs"><span></span><span></span><span></span><span></span><span></span></div>

</body>
</html>
```